Business Performance Improvement Book Cover Design Project

We need a book cover design for a new company, based in Eastern Australia, called Marrowby Global. We advise clients on process improvement, continuous improvement and business performance improvement, especially in the manufacturing areas and Fast Moving Consumer Goods industries.
We have a written a book designed to demonstrate our very high calibre of knowledge and to use as a marketing tool for prospective clients. We hope to give it out at training seminars and as a comprehensive business card.

Title of the book is: A holistic approach to Business Performance Improvement.
Subtitle: Tailor a Continuous Improvement approach to suit your company culture.
Author: by Gordon Marrowby
Back Cover: No need for a bar code in this edition. An important aspect is that we will distribute by hand. Text below for back page.

'For the experienced Business Performers, this book is designed to offer an insight into the advantages and an example of an approach to Business Improvement. It is not the only way but it is tried and tested in world class companies and it works. For those new to Continuous Improvement, it offers a helpful introduction to a holistic business improvement system, an overview of important success factors and pitfalls, recommendations on how to implement tools and methods and a quick guide to see when to use which tools. '

'Consultancies are one of many tools management teams can engage and management must make sure the consultants tailor their approach to suit its business needs and culture and not vice versa.'

End of text for back cover.

Business Performance Improvement is also known as or can include:
Continuous Improvement
Process Improvement
Lean Six Sigma
Operational Excellence
Total Productive Maintenance
Hadeko Assembly Method
Total Quality Management
Business Process Re engineering
Output Ladder
=
Marrowby Global

The book size is 175 x 240 mm and will need a 10-15mm bleed. The spine is not known at this stage exactly and will need to be updated once the printing is finished but I suggest a 10mm until I have the exact size.

Our company colours are Pantone 288, R0,G75,B141, C100,M79,Y17,K3. Attached are some other publications that give a sense of what we like to portray, Some words which might add to this are: professional, elegance, quality, sleek.
Updates

Reason: After receiving the designs, I realised that I needed to update the brief with more and better quality information for designers to work with.

Target Market(s)

people in the accounting and insolvency industries, production managers and CEOs, Chief Operating Officers, members of the executive team of large companies and GMs of small companies.

Industry/Entity Type

Marketing

Requirements
Must have
• Communicate an image that shows an improvement or increase of something.
Very professional and elegant
Emphasis on the words 'Business Performance Improvement' in the title, subtitle also important
Must appeal to a high-end of the market audience
Nice to have
• Recommendation for your cover to be gloss or matt in print
Image can be indirectly related to money but not specifically
Somehow that it matches or is not so different to the attached brochure
Should not have
• Not be too loud or commercial
Book jacket. WIll be printed as soft cover first run and hard cover 2nd run

```html
<!DOCTYPE html>
<html lang="en">
<head>
<meta charset="utf-8">
<title>A holistic approach to Business Performance Improvement — Front Cover</title>
<link rel="stylesheet" href="https://fonts.googleapis.com/css2?family=Cormorant+Garamond:ital,wght@1,500&family=Open+Sans:wght@300;400&display=swap">
<style>
  :root {
    --stage: #ffffff;
    --cover-deep: #0b4a86;
    --cover-mid: #1464a8;
    --cover-light: #2a86c8;
    --sky-glow: #4aa6e0;
    --chart-line: #7fd0f5;
    --chart-arrow: #bfe9fb;
    --ink-light: #ffffff;
    --ink-soft: #d6e8f6;
    --rule: rgba(255, 255, 255, 0.75);
  }
  * { box-sizing: border-box; margin: 0; padding: 0; }
  html, body {
    width: 1200px; height: 900px; overflow: hidden;
    background: var(--stage);
  }
  .canvas {
    position: relative; width: 1200px; height: 900px;
    display: flex; align-items: center; justify-content: center;
  }
  .cover {
    position: relative; width: 584px; height: 800px; overflow: hidden;
    background: linear-gradient(180deg, var(--cover-mid) 0%, var(--cover-deep) 100%);
    box-shadow: 0 6px 24px rgba(0, 40, 90, 0.18);
  }
  .cover__photo {
    position: absolute; left: 0; top: 0; width: 100%; height: 440px;
    background:
      radial-gradient(ellipse at 70% 35%, var(--sky-glow) 0%, transparent 60%),
      linear-gradient(160deg, var(--cover-light) 0%, var(--cover-mid) 55%, var(--cover-deep) 100%);
  }
  .cover__chart { position: absolute; left: 0; top: 120px; width: 100%; height: 200px; }
  .cover__band {
    position: absolute; left: 0; top: 440px; width: 100%; height: 360px;
    background: linear-gradient(180deg, rgba(20, 100, 168, 0.95) 0%, var(--cover-deep) 100%);
  }
  .cover__text { position: absolute; left: 44px; right: 40px; top: 462px; color: var(--ink-light); }
  .cover__author {
    font-family: "Open Sans", sans-serif; font-weight: 300; font-size: 16px; letter-spacing: 0.2px;
    padding-bottom: 8px; border-bottom: 1px solid var(--rule); display: inline-block; padding-right: 30px;
  }
  .cover__title {
    margin-top: 12px;
    font-family: "Cormorant Garamond", serif; font-style: italic; font-weight: 500;
    font-size: 36px; line-height: 1.08;
  }
  .cover__subtitle {
    margin-top: 16px; width: 210px;
    font-family: "Open Sans", sans-serif; font-weight: 300; font-size: 16px; line-height: 1.25;
    color: var(--ink-soft);
  }
  .cover__publisher {
    position: absolute; right: 40px; bottom: 52px;
    display: flex; align-items: center; gap: 10px;
    font-family: "Cormorant Garamond", serif; font-style: italic; font-weight: 500;
    font-size: 26px; color: var(--ink-light);
  }
  .cover__publisher-mark {
    width: 22px; height: 22px; border-radius: 50%; border: 2px solid var(--ink-light);
  }
</style>
</head>
<body>
<main class="canvas">
  <article class="cover">
    <div class="cover__photo" role="img" aria-label="Photograph of a businessman in a dark suit and blue tie drawing a rising line with a pen over a faint world map"></div>
    <svg class="cover__chart" viewBox="0 0 584 200" aria-hidden="true">
      <polyline points="0,150 50,130 95,160 150,95 195,120 250,80 300,98 345,58 400,72 450,30"
        fill="none" stroke="var(--chart-line)" stroke-width="9" stroke-linejoin="round" stroke-linecap="round" opacity="0.85"/>
      <polygon points="470,18 440,22 452,44" fill="var(--chart-arrow)"/>
    </svg>
    <div class="cover__band"></div>
    <section class="cover__text">
      <p class="cover__author">Gordon Marrowby B. Mech Eng., M. Sc (HSZ)</p>
      <h1 class="cover__title">A holistic approach to Business Performance Improvement.</h1>
      <p class="cover__subtitle">Tailor a Continuous Improvement approach to suit your company culture.</p>
    </section>
    <div class="cover__publisher">
      <span class="cover__publisher-mark"></span>
      <span class="cover__publisher-name">Marrowby Global</span>
    </div>
  </article>
</main>
</body>
</html>
```